Flaggendesign 1500 x 4000mm
Zielgruppe
Wir sind Lohnhersteller für Flüssigkeiten und Nahrungsergänzungmittel
Aufgabenstellung
Flaggendesign 1500mm x 4000mm
Die Druckvorgaben stehen in der PDF Datei beschrieben
Nach Möglichkeit das Logo in weiß / orange verwenden.

```html
<!DOCTYPE html>
<html lang="de">
<head>
<meta charset="utf-8">
<title>Norvetta – Flaggendesign</title>
<link rel="stylesheet" href="https://fonts.googleapis.com/css2?family=Open+Sans:wght@600;800&display=swap">
<style>
  :root {
    --navy-top: #0b5283;
    --navy-mid: #123f73;
    --navy-bottom: #24275a;
    --orange: #f0820f;
    --white: #ffffff;
    --page: #ffffff;
  }
  * { margin: 0; padding: 0; box-sizing: border-box; }
  html, body {
    width: 893px;
    height: 1200px;
    overflow: hidden;
    background: var(--page);
  }
  .flag {
    position: absolute;
    left: 189px;
    top: 0;
    width: 515px;
    height: 1200px;
    background: linear-gradient(180deg, var(--navy-top) 0%, var(--navy-mid) 55%, var(--navy-bottom) 100%);
    overflow: hidden;
  }
  .flag__band {
    position: absolute;
    right: 0;
    top: 0;
    width: 71px;
    height: 100%;
    background: var(--orange);
  }
  .flag__texture {
    position: absolute;
    left: 80px;
    width: 300px;
    height: 200px;
  }
  .flag__texture--top {
    top: 0;
    background: radial-gradient(ellipse at 60% 30%, rgba(150,170,210,0.22), rgba(150,170,210,0) 70%);
  }
  .flag__texture--bottom {
    bottom: 0;
    background: radial-gradient(ellipse at 50% 70%, rgba(150,170,210,0.22), rgba(150,170,210,0) 70%);
  }
  .flag__content {
    position: absolute;
    left: 0;
    top: 1200px;
    width: 1200px;
    height: 515px;
    transform: rotate(-90deg);
    transform-origin: top left;
    font-family: "Open Sans", sans-serif;
    color: var(--white);
  }
  .brand-name {
    position: absolute;
    left: 100px;
    top: 100px;
    font-size: 232px;
    font-weight: 800;
    line-height: 1;
    letter-spacing: -6px;
    color: var(--white);
  }
  .services {
    position: absolute;
    left: 134px;
    top: 385px;
    font-size: 18.5px;
    font-weight: 600;
    letter-spacing: 1.6px;
    white-space: nowrap;
  }
  .services__mark { color: var(--orange); }
  .services__item { margin-right: 14px; }
  .tagline {
    position: absolute;
    left: 245px;
    top: 461px;
    font-size: 30px;
    font-weight: 600;
    letter-spacing: 2.4px;
    white-space: nowrap;
  }
</style>
</head>
<body>
  <div class="flag">
    <div class="flag__texture flag__texture--top" role="img" aria-label="Dezentes Wabenmuster aus Linien"></div>
    <div class="flag__texture flag__texture--bottom" role="img" aria-label="Dezentes Wabenmuster aus Linien"></div>
    <div class="flag__band"></div>
    <div class="flag__content">
      <div class="brand-name">Norvetta</div>
      <div class="services">
        <span class="services__item"><span class="services__mark">»</span>LOHNFERTIGUNG</span>
        <span class="services__item"><span class="services__mark">»</span>LOHNABFÜLLUNG</span>
        <span class="services__item"><span class="services__mark">»</span>PRODUKTPLANUNG</span>
        <span class="services__item"><span class="services__mark">»</span>KONFEKTIONIERUNG</span>
      </div>
      <div class="tagline">IHR PRODUKT IN UNSERER FERTIGUNG</div>
    </div>
  </div>
</body>
</html>
```